Tarvel electrical letter head

Require a letter head to go with our new logo for our start up company. Something fresh and professional looking, also perhaps a "ghost"image of the logo in the centre of the page. Address to go on it PO Box 58, Tarrowvale 7563. Web address: www.tarvel.net.nz

```html
<!DOCTYPE html>
<html lang="en">
<head>
<meta charset="UTF-8">
<title>Tarvel Electrical – Letterhead</title>
<link rel="stylesheet" href="https://fonts.googleapis.com/css2?family=Open+Sans:wght@700&display=swap">
<style>
  :root {
    --paper: #ffffff;
    --brand-blue: #3d78c2;
    --brand-green: #a6cf38;
    --ghost: #e9eff7;
    --ink: #1a1a1a;
  }
  * { margin: 0; padding: 0; box-sizing: border-box; }
  html, body {
    width: 1071px;
    height: 1200px;
    overflow: hidden;
    background: var(--paper);
  }
  .letterhead {
    position: relative;
    width: 1071px;
    height: 1200px;
    background: var(--paper);
    font-family: "Open Sans", Arial, sans-serif;
  }
  .edge-bands {
    position: absolute;
    left: 0;
    top: 0;
    width: 30px;
    height: 1200px;
  }
  .band-blue { fill: var(--brand-blue); }
  .band-green { fill: var(--brand-green); }
  .brand-name {
    position: absolute;
    left: 72px;
    top: 70px;
    display: flex;
    align-items: center;
    gap: 14px;
    font-size: 40px;
    font-weight: 700;
    color: var(--brand-blue);
    letter-spacing: 0.5px;
    white-space: nowrap;
  }
  .brand-dot {
    width: 22px;
    height: 22px;
    border-radius: 50%;
    background: var(--brand-blue);
  }
  .ghost-name {
    position: absolute;
    left: 0;
    right: 0;
    top: 560px;
    text-align: center;
    font-size: 62px;
    font-weight: 700;
    color: var(--ghost);
    letter-spacing: 1px;
    white-space: nowrap;
  }
  .contact {
    position: absolute;
    left: 72px;
    bottom: 48px;
    font-size: 18px;
    font-weight: 700;
    line-height: 1.3;
    color: var(--ink);
    white-space: nowrap;
  }
</style>
</head>
<body>
  <main class="letterhead">
    <svg class="edge-bands" viewBox="0 0 30 1200" aria-hidden="true">
      <polygon class="band-blue" points="0,0 22,0 22,560 0,590"/>
      <polygon class="band-green" points="0,610 22,580 22,1200 0,1200"/>
    </svg>

    <header class="brand-name">
      <span class="brand-dot"></span>
      <span>Tarvel Electrical</span>
    </header>

    <div class="ghost-name" aria-hidden="true">Tarvel Electrical</div>

    <footer class="contact">
      <p>PO Box 58, Tarrowvale 7563</p>
      <p>www.tarvel.net.nz</p>
    </footer>
  </main>
</body>
</html>
```